Brightfold Partners Website

Brightfold Partners (BP) provide Analytics & Enterprise Performance Management (EPM) advisory & consultancy services. We are passionate about data and making a difference for our clients by working in partnership with them, helping them on their journey to becoming an Brightfold Partner. We deliver insights which give our clients a competitive edge and a much deeper understanding of their organisation.

We need a website which shows who we are, what we do and how we do it.

www.brightfold-partners.example is our very basic website at the moment. We want to completely revamp it with a corporate look

```html
<!DOCTYPE html>
<html lang="en">
<head>
<meta charset="utf-8">
<title>Brightfold Partners</title>
<link href="https://fonts.googleapis.com/css2?family=Poppins:wght@300;400;500;600;700;800&display=swap" rel="stylesheet">
<style>
:root{
  --orange:#e07f35;
  --orange-dark:#c9621f;
  --ink:#111820;
  --navy:#0f1a24;
  --grey:#6c7178;
  --line:#d5d7da;
  --white:#ffffff;
  --pale:#f1f4f6;
}
*{margin:0;padding:0;box-sizing:border-box}
html,body{width:1200px;height:2869px;overflow:hidden}
body{position:relative;font-family:'Poppins',sans-serif;color:var(--ink);background:var(--white)}
.abs{position:absolute}
a{color:inherit;text-decoration:none}

/* hero */
.hero{left:0;top:0;width:1200px;height:525px;background:linear-gradient(110deg,#1b2a38 0%,#2a3d4f 45%,#1a2733 75%,#121c25 100%)}
.hero-photo{left:0;top:0;width:1200px;height:525px;background:radial-gradient(ellipse at 70% 40%,rgba(120,110,95,.45),transparent 60%),linear-gradient(90deg,rgba(10,18,26,.7),rgba(10,18,26,.2) 60%,rgba(10,18,26,.5))}
.brand{display:flex;align-items:center;gap:10px;font-weight:600;color:var(--white);letter-spacing:.04em;line-height:1.1}
.brand-dot{width:26px;height:26px;border-radius:50%;border:3px solid var(--white)}
.nav{right:266px;top:25px;display:flex;gap:34px;font-size:12px;font-weight:600;color:var(--white)}
.hero-title{left:237px;top:128px;color:var(--white);font-size:50px;font-weight:400;line-height:1.2}
.hero-title strong{display:block;color:var(--orange);font-size:70px;font-weight:700;line-height:1}
.hero-sub{left:237px;top:294px;color:var(--white);font-size:16px;letter-spacing:.01em}
.btn-hero{left:237px;top:345px;width:169px;height:50px;background:linear-gradient(180deg,#e48a44,var(--orange-dark));color:var(--white);font-size:13px;font-weight:500;display:flex;align-items:center;justify-content:center;gap:9px;border-radius:2px}

/* who */
.h2{font-size:56px;font-weight:400;line-height:1;letter-spacing:-.01em}
.h2 b{color:var(--orange);font-weight:700}
.who-title{left:208px;top:685px}
.who-text{left:208px;top:770px;width:350px;font-size:10.5px;line-height:1.7;color:var(--grey)}
.who-contact{left:208px;top:853px;font-size:11.5px;line-height:1.75;color:var(--ink);font-weight:500}
.who-contact span{color:var(--orange);font-weight:600}
.who-photo{left:637px;top:620px;width:394px;height:400px;border-radius:50%;background:radial-gradient(circle at 60% 40%,#5b6673,#263442 65%,#1a2430)}

/* what */
.what{left:0;top:1083px;width:1200px;height:730px;background:linear-gradient(90deg,#e9edf0 0%,#f8f9fa 25%,#ffffff 50%,#f8f9fa 75%,#e6eaed 100%)}
.what-title{left:0;top:1130px;width:1200px;text-align:center}
.what-text{left:390px;top:1208px;width:420px;text-align:center;font-size:10.5px;line-height:1.7;color:var(--grey)}
.diagram{left:380px;top:1330px}
.label{font-size:10px;font-weight:600;color:var(--ink);white-space:nowrap}
.center-photo{left:450px;top:1402px;width:300px;height:300px;border-radius:50%;background:radial-gradient(circle at 50% 80%,#f4f6f8,#aeb6bd 55%,#3b444c 100%);display:flex;align-items:center;justify-content:center}
.center-name{font-size:17px;font-weight:600;color:var(--orange);letter-spacing:.03em;line-height:1.1;text-align:left}

/* how */
.how-title{left:0;top:1892px;width:1200px;text-align:center}
.step{width:160px}
.step h3{font-size:15px;font-weight:500;margin-bottom:10px}
.step .num{width:38px;height:38px;border-radius:50%;background:var(--grey);border:4px solid #e2e3e5;color:var(--white);font-size:12px;font-weight:600;display:flex;align-items:center;justify-content:center}
.step .num.active{background:var(--orange-dark);border-color:#f3d6bf}
.step p{font-size:10.5px;line-height:1.45;color:var(--grey);margin-top:16px;width:150px}
.step-line{left:175px;top:2054px;width:760px;height:1px;background:var(--line)}

/* footer */
.footer-bg{left:0;top:2370px;width:1200px;height:499px;background:var(--navy);border-top-left-radius:190px 190px}
.cta{left:162px;top:2242px;width:875px;height:288px;background:linear-gradient(100deg,var(--orange-dark) 0%,#d9742d 60%,#e48a44 100%);border-bottom-right-radius:110px;border-top-left-radius:6px;border-top-right-radius:6px;border-bottom-left-radius:6px;overflow:hidden}
.cta-arc{left:520px;top:-40px;width:520px;height:420px;border-radius:50%;background:rgba(255,255,255,.06)}
.cta-title{left:0;top:50px;width:875px;text-align:center;color:var(--white);font-size:42px;font-weight:300;line-height:1.27}
.cta-title b{font-weight:700}
.btn{top:185px;width:168px;height:50px;display:flex;align-items:center;justify-content:center;gap:10px;font-size:13px;font-weight:500}
.btn-phone{left:256px;background:var(--white);color:var(--ink);border-bottom-right-radius:16px}
.btn-mail{left:452px;border:1.5px solid var(--white);color:var(--white)}
.foot-brand{left:163px;top:2588px;font-size:20px}
.foot-brand .brand-dot{width:44px;height:44px;border-width:5px}
.social{top:2676px;width:26px;height:26px;border-radius:50%;background:var(--orange-dark)}
.foot-h{font-size:18px;font-weight:500;color:var(--white)}
.foot-h::after{content:"";display:block;width:32px;height:2px;background:var(--orange);margin-top:8px}
.foot-links{left:600px;top:2652px;list-style:none;font-size:10.5px;color:var(--white);line-height:26.5px}
.divider{left:749px;top:2598px;width:1px;height:180px;background:#2c3844}
.addr{left:833px;font-size:10px;color:#d9dde1;display:flex;gap:12px;align-items:center;line-height:1.6}
.addr .ico{width:28px;height:28px;border-radius:50%;background:var(--orange-dark);display:flex;align-items:center;justify-content:center;flex:none}
.copy{left:0;top:2828px;width:1200px;text-align:center;font-size:10px;color:#c6cbd0}
.copy span{color:#4a7bd6;margin-left:14px}
</style>
</head>
<body>

<section>
  <div class="abs hero" role="img" aria-label="Photo of a team celebrating in a modern office at night"></div>
  <div class="abs hero-photo"></div>
  <div class="abs brand" style="left:163px;top:20px;font-size:10.5px"><span class="brand-dot"></span><span>BRIGHTFOLD<br>PARTNERS</span></div>
  <nav class="abs nav"><a>Home</a><a>Service</a><a>About us</a><a>Contact us</a></nav>
  <h1 class="abs hero-title">Brightfold<strong>Partners</strong></h1>
  <p class="abs hero-sub">DATA ANALYTICS &amp; EPM CONSULTING SERVICES</p>
  <a class="abs btn-hero"><svg width="20" height="15" viewBox="0 0 20 15" fill="none" stroke="#fff" stroke-width="1.6"><rect x="1" y="1" width="18" height="13" rx="1.5"/><path d="M1 2l9 7 9-7"/></svg>Contact us</a>
</section>

<section>
  <h2 class="abs h2 who-title"><b>Who</b> we are?</h2>
  <p class="abs who-text">Brightfold Partners is an exciting start-up in the Data Analytics and EPM space. Founded in 2019, BP specialise in the implementation and support of BI, EPM and Data Analytics business solutions, both in the Cloud and on-premise.</p>
  <p class="abs who-contact">Call us on: <span>01 555 0142</span> or<br>Email: <span>info@brightfold-partners.example</span><br>for more information</p>
  <div class="abs who-photo" role="img" aria-label="Photo of a smiling consultant working at a laptop"></div>
</section>

<section>
  <div class="abs what" role="img" aria-label="Faint background photo of city office towers"></div>
  <h2 class="abs h2 what-title"><b>What</b> we do?</h2>
  <p class="abs what-text">BP are a Data Analytics &amp; EPM company, specialising in the implementation and support of Business Intelligence, EPM and Data Analytics business solutions, both in the Cloud and on-premise</p>
  <svg class="abs diagram" width="440" height="440" viewBox="0 0 440 440">
    <circle cx="220" cy="222" r="200" fill="none" stroke="#b9bec3" stroke-width="1" stroke-dasharray="2 3"/>
  </svg>
  <div class="abs center-photo" role="img" aria-label="Photo looking up at skyscrapers">
    <div class="center-name">BRIGHTFOLD<br>PARTNERS</div>
  </div>
  <svg class="abs" style="left:572px;top:1322px" width="56" height="56" viewBox="0 0 56 56"><circle cx="28" cy="28" r="27" fill="#d46c26"/><circle cx="28" cy="28" r="22" fill="none" stroke="#fff" stroke-opacity=".5"/><circle cx="28" cy="27" r="8" fill="none" stroke="#fff" stroke-width="1.5"/><path d="M25 37h6" stroke="#fff" stroke-width="1.5"/></svg>
  <svg class="abs" style="left:370px;top:1524px" width="56" height="56" viewBox="0 0 56 56"><circle cx="28" cy="28" r="27" fill="#d46c26"/><circle cx="28" cy="28" r="22" fill="none" stroke="#fff" stroke-opacity=".5"/><path d="M20 36V30M26 36V26M32 36V22M38 36V18" stroke="#fff" stroke-width="2"/></svg>
  <svg class="abs" style="left:774px;top:1524px" width="56" height="56" viewBox="0 0 56 56"><circle cx="28" cy="28" r="27" fill="#d46c26"/><circle cx="28" cy="28" r="22" fill="none" stroke="#fff" stroke-opacity=".5"/><circle cx="24" cy="26" r="7" fill="none" stroke="#fff" stroke-width="1.5"/><path d="M22 36h4M32 24l8-8" stroke="#fff" stroke-width="1.5"/></svg>
  <div class="abs label" style="left:525px;top:1303px">ADVISE &amp; ARCHITECT SERVICES</div>
  <div class="abs label" style="left:260px;top:1546px">OPTIMISE &amp; MANAGE</div>
  <div class="abs label" style="left:840px;top:1546px">DESIGN &amp; IMPLEMENT</div>
</section>

<section>
  <h2 class="abs h2 how-title"><b>How</b> we do it?</h2>
  <div class="abs step-line"></div>
  <div class="abs step" style="left:155px;top:2002px"><h3>Title 01</h3><div class="num active">01</div><p>Lorem ipsum dolor sit amet, consectetur adipiscing elit, sed do eiusmod tempor incididunt</p></div>
  <div class="abs step" style="left:402px;top:2002px"><h3>Title 02</h3><div class="num">02</div><p>Lorem ipsum dolor sit amet, consectetur adipiscing elit, sed do eiusmod tempor incididunt</p></div>
  <div class="abs step" style="left:649px;top:2002px"><h3>Title 03</h3><div class="num">03</div><p>Lorem ipsum dolor sit amet, consectetur adipiscing elit, sed do eiusmod tempor incididunt</p></div>
  <div class="abs step" style="left:897px;top:2002px"><h3>Title 04</h3><div class="num">04</div><p>Lorem ipsum dolor sit amet, consectetur adipiscing elit, sed do eiusmod tempor incididunt</p></div>
</section>

<footer>
  <div class="abs footer-bg"></div>
  <div class="abs cta">
    <div class="abs cta-arc"></div>
    <h2 class="abs cta-title"><b>Contact us</b> to discuss your<br>business needs</h2>
    <a class="abs btn btn-phone"><svg width="18" height="18" viewBox="0 0 24 24"><path fill="#111820" d="M6.6 10.8a15.1 15.1 0 006.6 6.6l2.2-2.2a1 1 0 011-.25 11.4 11.4 0 003.6.57 1 1 0 011 1V20a1 1 0 01-1 1A17 17 0 013 4a1 1 0 011-1h3.5a1 1 0 011 1c0 1.25.2 2.45.57 3.57a1 1 0 01-.25 1z"/></svg>01 555 0142</a>
    <a class="abs btn btn-mail"><svg width="20" height="15" viewBox="0 0 20 15" fill="none" stroke="#fff" stroke-width="1.6"><rect x="1" y="1" width="18" height="13" rx="1.5"/><path d="M1 2l9 7 9-7"/></svg>Contact us</a>
  </div>

  <div class="abs brand foot-brand"><span class="brand-dot"></span><span>BRIGHTFOLD<br>PARTNERS</span></div>
  <a class="abs social" style="left:163px" aria-label="Professional network"></a>
  <a class="abs social" style="left:200px" aria-label="Social feed"></a>

  <div class="abs foot-h" style="left:600px;top:2596px">Explore</div>
  <ul class="abs foot-links"><li>Home</li><li>Service ▴</li><li>About us</li><li>Contact us</li></ul>
  <div class="abs divider"></div>

  <div class="abs foot-h" style="left:833px;top:2596px">Address</div>
  <div class="abs addr" style="top:2656px"><span class="ico"><svg width="12" height="14" viewBox="0 0 12 14"><path fill="#fff" d="M6 0a5 5 0 015 5c0 4-5 9-5 9S1 9 1 5a5 5 0 015-5zm0 3a2 2 0 100 4 2 2 0 000-4z"/></svg></span><span>14 Harbour Lane, Riverside,<br>Dublin 4, D04 KT21</span></div>
  <div class="abs addr" style="top:2697px"><span class="ico"><svg width="13" height="10" viewBox="0 0 20 15" fill="none" stroke="#fff" stroke-width="2"><rect x="1" y="1" width="18" height="13"/><path d="M1 2l9 7 9-7"/></svg></span><span>info@brightfold-partners.example</span></div>
  <div class="abs addr" style="top:2742px"><span class="ico"><svg width="12" height="12" viewBox="0 0 24 24"><path fill="#fff" d="M6.6 10.8a15.1 15.1 0 006.6 6.6l2.2-2.2a1 1 0 011-.25 11.4 11.4 0 003.6.57 1 1 0 011 1V20a1 1 0 01-1 1A17 17 0 013 4a1 1 0 011-1h3.5a1 1 0 011 1c0 1.25.2 2.45.57 3.57a1 1 0 01-.25 1z"/></svg></span><span>01 555 0142</span></div>

  <p class="abs copy">Copyright © 2022 Brightfold Partners. &nbsp;&nbsp; | <span>Privacy Policy.</span></p>
</footer>

</body>
</html>
```